Psychedelic Abstract Colorful Overgrowth Album Cover Art

An Abstract Psychedelic Album Cover for my Debut Album. Bright Colors. Includes the Album Title "Overgrowth" and artist name "Vex the Harbor". Abstract art no design restrictions whatsoever. Illustrate whatever the word "Overgrowth" brings to mind. Other then that no restrictions let your brain go wild lets see what you got !

Target Market(s)

Males ages 13-29

Requirements
Must have
• The Album title "Overgrowth" on the cover as well as the artist name "Vex the Harbor. Also Psychedelic Designs And Bright Colors.
Should not have
• NO Stock Images. Must Be 100% original design

```html
<!DOCTYPE html>
<html lang="en">
<head>
<meta charset="utf-8">
<title>Overgrowth — Vex the Harbor</title>
<link rel="preconnect" href="https://fonts.googleapis.com">
<link href="https://fonts.googleapis.com/css2?family=Antonio:wght@200;300&display=swap" rel="stylesheet">
<style>
  :root {
    --cream: #f0e2bc;
    --red: #e0242f;
    --orange: #f08a1c;
    --olive: #b7b72a;
    --green: #2fb82a;
    --magenta: #b0208f;
    --purple: #6a22b0;
    --blue: #2b3fb8;
    --teal: #1f6f86;
    --title: #e6e6ea;
    --artist: #1d3461;
  }
  * { margin: 0; padding: 0; box-sizing: border-box; }
  html, body {
    width: 1200px;
    height: 1200px;
    overflow: hidden;
    background: var(--cream);
  }
  .cover {
    position: relative;
    width: 1200px;
    height: 1200px;
    overflow: hidden;
  }
  .cover-art {
    position: absolute;
    inset: 0;
    background:
      radial-gradient(ellipse 38% 26% at 88% 38%, var(--green), rgba(47,184,42,0) 75%),
      radial-gradient(ellipse 34% 20% at 70% 12%, var(--olive), rgba(183,183,42,0) 75%),
      radial-gradient(ellipse 36% 22% at 35% 22%, var(--orange), rgba(240,138,28,0) 75%),
      radial-gradient(ellipse 34% 24% at 12% 42%, var(--red), rgba(224,36,47,0) 75%),
      radial-gradient(ellipse 30% 18% at 30% 58%, var(--red), rgba(224,36,47,0) 75%),
      radial-gradient(ellipse 34% 22% at 18% 80%, var(--magenta), rgba(176,32,143,0) 75%),
      radial-gradient(ellipse 28% 22% at 50% 82%, var(--purple), rgba(106,34,176,0) 75%),
      radial-gradient(ellipse 30% 20% at 82% 74%, var(--blue), rgba(43,63,184,0) 75%),
      radial-gradient(ellipse 22% 14% at 62% 68%, var(--teal), rgba(31,111,134,0) 75%),
      linear-gradient(160deg, var(--olive) 0%, var(--orange) 22%, var(--red) 40%, var(--cream) 58%, var(--cream) 64%, var(--purple) 82%, var(--blue) 100%);
  }
  .cover-type {
    position: absolute;
    inset: 0;
    width: 1200px;
    height: 1200px;
  }
  .album-title {
    font-family: "Antonio", "Arial Narrow", sans-serif;
    font-weight: 200;
    font-size: 76px;
    fill: var(--title);
  }
  .artist-name {
    font-family: "Antonio", "Arial Narrow", sans-serif;
    font-weight: 300;
    font-size: 168px;
    fill: var(--artist);
  }
</style>
</head>
<body>
  <main class="cover">
    <div class="cover-art" role="img" aria-label="Abstract painted illustration of vivid sweeping diagonal brush-stroke stripes in red, orange, green, magenta, purple and blue over a cream ground, like wild overgrowth"></div>
    <svg class="cover-type" viewBox="0 0 1200 1200">
      <text class="album-title" x="128" y="136" textLength="990" lengthAdjust="spacing">OVERGROWTH</text>
      <text class="artist-name" x="50" y="1156" textLength="1102" lengthAdjust="spacing">VEX THE HARBOR</text>
    </svg>
  </main>
</body>
</html>
```